Business Card Design

redesign of card and recreation of logo based on image provided. the business is located in new york so the Brooklyn Bridge figures prominently in the scheme. product should be very clean.

Industry/Entity Type

Real Estate

Contact Information for Business Card

Wendell Ortwick 318 Tamsin Street Brooklyn, New York 11409 wendell@qorvane.com Mobile: 917-555-0143

Colors
cadf82
1b1b1b
ffffff

Requirements
Nice to have
• Brooklyn Bridge

```html
<!DOCTYPE html>
<html lang="en">
<head>
<meta charset="utf-8">
<title>Halvern &amp; Assoc. — Business Card</title>
<link rel="stylesheet" href="https://fonts.googleapis.com/css2?family=Open+Sans:wght@400;600&display=swap">
<style>
  :root {
    --olive: #aea714;
    --olive-dark: #8c8a1c;
    --ink: #1b1b1b;
    --paper: #f1f1f1;
    --paper-shade: #dcdcdc;
    --backdrop: #e4e4e4;
    --sketch: #c9c6c2;
    --white: #ffffff;
  }
  * { box-sizing: border-box; margin: 0; padding: 0; }
  html, body {
    width: 1189px; height: 1200px; overflow: hidden;
    background: var(--backdrop);
    font-family: "Open Sans", sans-serif;
  }
  .card {
    position: absolute; left: 140px; width: 917px; height: 522px;
    overflow: hidden;
  }
  .card--front { top: 45px; background: linear-gradient(180deg, #f4f4f4, #e6e6e6); }
  .card--back { top: 624px; background: var(--olive-dark); padding: 14px 20px; }

  .bridge-art {
    position: absolute;
    background: linear-gradient(180deg, rgba(0,0,0,0) 0%, var(--sketch) 55%, rgba(0,0,0,0) 100%);
    opacity: .8;
  }
  .card--front .bridge-art { left: 170px; top: 25px; width: 547px; height: 160px; }

  .wordmark {
    position: absolute; white-space: nowrap;
    color: var(--olive); font-weight: 400; letter-spacing: -1px;
  }
  .card--front .wordmark { left: 170px; top: 182px; font-size: 52px; }

  .wave { position: absolute; left: 0; top: 0; width: 917px; height: 522px; }

  .holder { position: absolute; left: 30px; top: 395px; color: var(--white); }
  .holder__name { font-size: 44px; letter-spacing: 3px; line-height: 1.1; }
  .holder__title { font-size: 32px; letter-spacing: 2px; line-height: 1.2; }

  .contact { position: absolute; right: 25px; top: 360px; list-style: none; }
  .contact li {
    display: flex; justify-content: flex-end; align-items: center;
    height: 32px; color: var(--white); font-size: 24px; font-weight: 600;
    letter-spacing: 2px;
  }
  .contact .icon {
    width: 20px; height: 20px; margin-left: 26px;
    background: var(--white); border-radius: 2px; flex: none;
  }
  .contact .icon svg { display: block; width: 20px; height: 20px; }
  .contact .icon--none { background: none; }

  .back__panel {
    position: relative; width: 100%; height: 100%;
    background: radial-gradient(ellipse at 55% 20%, #fafafa, #e2e0e2);
  }
  .card--back .bridge-art { left: 40px; top: 40px; width: 806px; height: 270px; }
  .card--back .wordmark { left: 40px; top: 300px; font-size: 86px; }
</style>
</head>
<body>

<section class="card card--front">
  <div class="bridge-art" role="img" aria-label="Pencil sketch of a suspension bridge"></div>
  <div class="wordmark">Halvern &amp; Assoc.</div>

  <svg class="wave" viewBox="0 0 917 522" aria-hidden="true">
    <path d="M0 277 C120 330 260 360 420 330 C560 300 660 270 760 272 L760 522 L0 522 Z" fill="var(--ink)"/>
    <path d="M0 347 C150 365 300 360 460 330 C600 300 700 270 780 275 C850 280 890 300 917 318 L917 522 L0 522 Z" fill="var(--olive)"/>
  </svg>

  <div class="holder">
    <p class="holder__name">Wendell Ortwick</p>
    <p class="holder__title">Broker</p>
  </div>

  <ul class="contact">
    <li>917-555-0143
      <span class="icon"><svg viewBox="0 0 20 20"><path d="M6 4 L8 4 L9 7 L7.5 8.5 C8.3 10.5 9.5 11.7 11.5 12.5 L13 11 L16 12 L16 14 C16 15 15 16 14 16 C8.5 15.5 4.5 11.5 4 6 C4 5 5 4 6 4 Z" fill="var(--olive)"/></svg></span>
    </li>
    <li>wendell@qorvane.com
      <span class="icon"><svg viewBox="0 0 20 20"><rect x="4" y="6" width="12" height="8" fill="none" stroke="var(--olive)" stroke-width="1.5"/><path d="M4 6 L10 11 L16 6" fill="none" stroke="var(--olive)" stroke-width="1.5"/></svg></span>
    </li>
    <li>318 Tamsin Street
      <span class="icon"><svg viewBox="0 0 20 20"><path d="M10 16 C7 12 6 10 6 8.5 A4 4 0 0 1 14 8.5 C14 10 13 12 10 16 Z" fill="var(--olive)"/><circle cx="10" cy="8.5" r="1.5" fill="var(--white)"/></svg></span>
    </li>
    <li>Brooklyn, New York 11409<span class="icon icon--none"></span></li>
  </ul>
</section>

<section class="card card--back">
  <div class="back__panel">
    <div class="bridge-art" role="img" aria-label="Pencil sketch of a suspension bridge"></div>
    <div class="wordmark">Halvern &amp; Assoc.</div>
  </div>
</section>

</body>
</html>
```